VORALUX SYSTEMS BUSINESS CARD DESIGN

WE WANT COMPLETE NEW DESIGN OF OUR BUSINESS CARD. WE ARE AN INTEGRATION COMPANY, WHERE WE INTEGRATE IOT/SMART SYSTEMS TO HOMES AND CORPORATE CUSTOMERS. WE SUPPLY AND INSTALL AUTOMATION PRODUCTS. THE FINAL DESIGN SHOULD COMMUNICATE TECHNOLOGY. THE CARD DESIGN SHOULD BE VERY IMPACT FULL. LOGO NEEDS TO BE THERE. IT WOULD NICE IF THE DESIGN WAS CLEAN. COLORS IS UP TO DESIGNER TO PLAY WITH, OR CAN STICK TO CORPORATE COLORS (FOLLOW LOGO). I HAVE ADDED FEW REFERENCE PHOTOS TO DRAW INSPIRATION MAYBE. I HAVE ADDED A HEX DESIGN, ITS NOT NECESSARY TO USE THIS DESIGN, ITS UPTO DESIGNER, JUST ADDED IF NEEDED TO PLAY WITH DESIGN.

Target Market(s)

Private end users and corporate clients

Industry/Entity Type

technology, home automation, home theaters, building management systems, IOT

Contact Information for Business Card

It should include Employee name, personal number, office number, email address, both in English and arabic. DETAILS TO INCLUDE :DANIEL MARUVEN, MOBILE 0097150738219,OFFCIE 009714368174, DANIEL@VORALUXSYS.CO

Requirements
Must have
• Should feel like a technology company from design. Details both and in English and arabic (or at least have provision for arabic in design).
Nice to have
• I would like logo on one side, and details on the other side. Logo design side should communicate technology with logo. Other side can be clean just with information or also have some design aspects following from logo side. it would be interesting to see submissions with square design as well (that looks like an app Icon). colors could be of logo, red black grey and white. I have added some designs to draw inspiration from

```html
<!DOCTYPE html>
<html lang="en">
<head>
<meta charset="utf-8">
<title>Voralux Systems – Business Card</title>
<link rel="stylesheet" href="https://fonts.googleapis.com/css2?family=Michroma&family=Roboto:wght@400;700&display=swap">
<style>
  :root {
    --backdrop: #2c2c2c;
    --card: #ececec;
    --ink: #141414;
    --red: #d0161f;
    --facet-a: #1fb58f;
    --facet-b: #3fd0e0;
    --facet-c: #f0c21a;
    --facet-d: #e3222b;
    --facet-e: #3a2a6e;
  }
  html, body {
    margin: 0;
    padding: 0;
    width: 1200px;
    height: 1138px;
    overflow: hidden;
    background: var(--backdrop);
  }
  .stage {
    position: relative;
    width: 1200px;
    height: 1138px;
  }
  .card {
    position: absolute;
    background: linear-gradient(160deg, #f3f3f3 0%, var(--card) 60%, #e2e2e2 100%);
    border-radius: 14px;
    overflow: hidden;
  }
  .card--front { left: 272px; top: 184px; width: 622px; height: 376px; }
  .card--back  { left: 274px; top: 606px; width: 619px; height: 375px; }

  .brand {
    position: absolute;
    z-index: 2;
    display: flex;
    align-items: center;
    gap: 8px;
    font-family: "Roboto", Arial, sans-serif;
    font-weight: 700;
    line-height: 1;
    color: var(--ink);
    letter-spacing: 0.5px;
    white-space: nowrap;
  }
  .brand__dot {
    width: 22px;
    height: 22px;
    border-radius: 50%;
    background: var(--red);
    flex: none;
  }
  .card--front .brand { left: 48px; top: 118px; font-size: 21px; }
  .card--back .brand  { left: 30px; top: 60px; font-size: 24px; }
  .card--back .brand__dot { width: 26px; height: 26px; }

  .tagline {
    position: absolute;
    z-index: 2;
    font-family: "Michroma", Arial, sans-serif;
    line-height: 1;
    color: var(--ink);
    white-space: nowrap;
  }
  .card--front .tagline { left: 46px; top: 166px; font-size: 10px; letter-spacing: 1px; }
  .card--back .tagline  { left: 28px; top: 118px; font-size: 12px; letter-spacing: 1.5px; }

  .facets {
    position: absolute;
    z-index: 1;
    background:
      radial-gradient(circle at 25% 75%, var(--facet-d) 0%, transparent 40%),
      radial-gradient(circle at 75% 30%, var(--facet-b) 0%, transparent 45%),
      radial-gradient(circle at 55% 80%, var(--facet-c) 0%, transparent 40%),
      radial-gradient(circle at 90% 85%, var(--facet-e) 0%, transparent 45%),
      linear-gradient(135deg, var(--facet-a), var(--facet-e));
  }
  .card--front .facets { left: 310px; top: 54px; width: 272px; height: 268px; }
  .card--back .facets  { left: 328px; top: 54px; width: 268px; height: 290px; }

  .person {
    position: absolute;
    left: 28px;
    top: 204px;
    margin: 0;
    font-family: "Roboto", Arial, sans-serif;
    font-weight: 700;
    font-size: 24px;
    line-height: 1.2;
    color: var(--red);
  }
  .contacts {
    position: absolute;
    left: 34px;
    top: 246px;
    margin: 0;
    padding: 0;
    list-style: none;
    font-family: "Roboto", Arial, sans-serif;
    font-size: 16px;
    color: var(--ink);
  }
  .contacts li {
    display: flex;
    align-items: center;
    height: 24px;
    white-space: nowrap;
  }
  .contacts svg {
    width: 13px;
    height: 13px;
    margin-right: 15px;
    fill: none;
    stroke: var(--red);
    stroke-width: 2;
  }
</style>
</head>
<body>
<div class="stage">

  <section class="card card--front">
    <div class="brand"><span class="brand__dot"></span>VORALUX SYSTEMS</div>
    <div class="tagline">A VORALUX GROUP DIVISION.</div>
    <div class="facets" role="img" aria-label="Large multicoloured faceted crystal pattern decoration"></div>
  </section>

  <section class="card card--back">
    <div class="brand"><span class="brand__dot"></span>VORALUX SYSTEMS</div>
    <div class="tagline">A VORALUX GROUP DIVISION.</div>
    <h1 class="person">Daniel Maruven</h1>
    <ul class="contacts">
      <li><svg viewBox="0 0 16 16"><rect x="4" y="1" width="8" height="14" rx="1.5"/><line x1="7" y1="12" x2="9" y2="12"/></svg>0097150738219</li>
      <li><svg viewBox="0 0 16 16"><circle cx="8" cy="8" r="6.5"/><path d="M5.5 5 L7 5 L7.5 7 L6.7 7.8 Q7.5 9.3 8.8 9.9 L9.6 9 L11.2 9.6 L11 11 Q7 11 5 6.5 Z"/></svg>009714368174</li>
      <li><svg viewBox="0 0 16 16"><rect x="1.5" y="3.5" width="13" height="9"/><path d="M1.5 3.5 L8 9 L14.5 3.5"/></svg>daniel@voraluxsys.co</li>
      <li><svg viewBox="0 0 16 16"><circle cx="8" cy="8" r="6.5"/><ellipse cx="8" cy="8" rx="2.8" ry="6.5"/><line x1="1.5" y1="8" x2="14.5" y2="8"/></svg>www.voraluxsys.co</li>
    </ul>
    <div class="facets" role="img" aria-label="Multicoloured faceted crystal pattern decoration"></div>
  </section>

</div>
</body>
</html>
```